LA Billboard Project for Brisk Lending

We are running three different billboards around LA, and we need someone to take the mock-ups I've created and bring this campaign to life. Whatever wording is on the mock-ups should stay the same in the ads you create, but feel free to get creative with layout and style. I've attached our mock-ups, our style guide, our logo, and the necessary specs for the billboards. If you have any questions, feel free to reach out!

```html
<!DOCTYPE html>
<html lang="en">
<head>
<meta charset="utf-8">
<title>Brisk Lending – Mortgage Made Simple Billboard</title>
<link href="https://fonts.googleapis.com/css2?family=Montserrat:wght@400;500;600;700;800&display=swap" rel="stylesheet">
<style>
  :root {
    --page-bg: #e9edf2;
    --navy: #1d3050;
    --navy-deep: #172741;
    --teal: #3fc1c4;
    --yellow: #f7d31c;
    --white: #ffffff;
    --band-text: #1d3050;
  }
  * { margin: 0; padding: 0; box-sizing: border-box; }
  html, body {
    width: 1200px;
    height: 798px;
    overflow: hidden;
    background: var(--page-bg);
    font-family: "Montserrat", Arial, sans-serif;
  }
  .billboard {
    position: absolute;
    left: 40px;
    top: 166px;
    width: 1120px;
    height: 466px;
    background: radial-gradient(ellipse at 30% 40%, #22385b 0%, var(--navy) 55%, var(--navy-deep) 100%);
    overflow: hidden;
  }
  .billboard-shapes {
    position: absolute;
    inset: 0;
    width: 1120px;
    height: 466px;
  }
  .brand-name {
    position: absolute;
    left: 20px;
    top: 50px;
    width: 380px;
    text-align: center;
    color: var(--teal);
    font-weight: 700;
    font-size: 44px;
    letter-spacing: -0.5px;
    line-height: 1.05;
  }
  .headline {
    position: absolute;
    left: 20px;
    top: 192px;
    width: 380px;
    text-align: center;
    color: var(--yellow);
    font-weight: 700;
    font-size: 40px;
    line-height: 1.08;
    letter-spacing: 0.5px;
  }
  .subline {
    position: absolute;
    left: 20px;
    top: 312px;
    width: 380px;
    text-align: center;
    color: var(--white);
    font-weight: 500;
    font-size: 18px;
    line-height: 1.3;
  }
  .contact-band {
    position: absolute;
    left: 0;
    bottom: 0;
    width: 1120px;
    height: 70px;
    display: flex;
    align-items: center;
    justify-content: center;
    gap: 40px;
    color: var(--band-text);
    font-weight: 700;
    font-size: 34px;
    letter-spacing: 2px;
  }
  .contact-divider {
    width: 4px;
    height: 38px;
    background: var(--band-text);
  }
</style>
</head>
<body>
  <div class="billboard">
    <svg class="billboard-shapes" viewBox="0 0 1120 466" xmlns="http://www.w3.org/2000/svg">
      <defs>
        <linearGradient id="house-photo-tone" x1="0" y1="0" x2="0.3" y2="1">
          <stop offset="0" stop-color="#3b3f6e"/>
          <stop offset="0.35" stop-color="#4c5f7c"/>
          <stop offset="0.65" stop-color="#2f8a9a"/>
          <stop offset="1" stop-color="#1c3a3a"/>
        </linearGradient>
      </defs>
      <rect class="band-stripe" x="0" y="386" width="1120" height="10" fill="var(--teal)"/>
      <rect class="band-fill" x="0" y="396" width="1120" height="70" fill="var(--yellow)"/>
      <path class="accent-teal" d="M416 0 C346 120 350 312 546 386 L1120 386 L1120 0 Z" fill="var(--teal)"/>
      <path class="accent-yellow" d="M432 0 C364 120 368 306 562 386 L1120 386 L1120 0 Z" fill="var(--yellow)"/>
      <path class="hero-photo" role="img" aria-label="Modern two-storey luxury home at dusk with glass walls and a lit turquoise swimming pool"
            d="M446 0 C382 120 388 300 590 386 L1120 386 L1120 0 Z" fill="url(#house-photo-tone)"/>
    </svg>

    <div class="brand-name">Brisk<br>Lending</div>
    <h1 class="headline">MORTGAGE<br>MADE SIMPLE</h1>
    <p class="subline">We take you step-by-step to get<br>your home loan done right</p>

    <div class="contact-band">
      <span class="contact-phone">800-555-0147</span>
      <span class="contact-divider"></span>
      <span class="contact-email">help@brisklending.com</span>
    </div>
  </div>
</body>
</html>
```